Business Card & Letterhead Design

We a financial advice company based in Australia. We provide advice to wealthy farmers.

We are changing our business name FROM Brightmere Financial TO Calderstone Wealth and we need a new letterhead and double sided business card design

Attached is designs from our previous branding (Brightmere Financial) as it includes all the details we require on the new Calderstone Wealth business cards and letterhead.

```html
<!DOCTYPE html>
<html lang="en">
<head>
<meta charset="utf-8">
<title>Calderstone Wealth Stationery</title>
<link rel="stylesheet" href="https://fonts.googleapis.com/css2?family=Marcellus&family=Montserrat:wght@400;500;600;700&display=swap">
<style>
:root{
  --backdrop:#3f4a54;
  --paper:#f1f1f2;
  --ink:#2e2e30;
  --ink-soft:#55575b;
  --charcoal:#2f2f32;
  --slate:#4b5259;
  --slate-light:#6a7178;
  --footer-text:#e3e5e7;
}
*{margin:0;padding:0;box-sizing:border-box}
html,body{width:1200px;height:1019px;overflow:hidden}
body{background:var(--backdrop);font-family:"Montserrat",sans-serif;color:var(--ink);position:relative}
.abs{position:absolute}

/* Letterhead */
.letterhead{position:absolute;left:209px;top:159px;width:525px;height:699px;background:var(--paper);overflow:hidden}
.brand-mark{position:absolute;border:2px solid var(--ink);border-radius:50%}
.brand-name{font-family:"Marcellus",serif;font-weight:400;color:var(--ink);white-space:nowrap;letter-spacing:.02em;line-height:1}
.brand-tagline{font-family:"Montserrat",sans-serif;color:var(--ink-soft);white-space:nowrap;letter-spacing:.32em;text-transform:uppercase;line-height:1}
.lh-mark{left:129px;top:40px;width:66px;height:66px}
.lh-name{left:0;width:324px;text-align:center;top:108px;font-size:22px}
.lh-tagline{left:0;width:324px;text-align:center;top:133px;font-size:8.2px}
.motto{left:372px;top:48px;width:120px;height:13px;background:var(--slate);color:#fff;font-size:7.6px;font-weight:600;text-align:center;line-height:13px}
.entity{right:33px;text-align:right;font-size:7px;line-height:8.8px;letter-spacing:.06em;color:var(--ink-soft)}
.entity.trading{top:64px}
.entity.abn{top:95px;font-weight:700;color:var(--ink);font-size:7.4px}
.entity.rep{top:107px}
.letter-body{left:35px;top:205px;width:457px;font-size:7.65px;line-height:10.6px;text-align:justify;color:var(--ink)}
.letter-body p{margin-bottom:10.5px}
.signature{left:399px;top:509px;width:100px;height:28px;background:linear-gradient(90deg,#e4e4e5,#d9d9db)}
.footer-art{left:0;top:572px;width:525px;height:127px}
.footer-text{color:var(--footer-text);font-size:7.4px;line-height:9.2px;letter-spacing:.08em;white-space:nowrap}
.web{left:36px;top:575px;font-size:8.6px;line-height:10.2px}
.phones{left:36px;top:618px;font-size:8.2px;line-height:10px}
.address{left:36px;top:649px}
.licensee{right:33px;text-align:right;top:619px;font-size:8.2px;line-height:10px}
.licence{right:33px;text-align:right;top:649px;font-size:7.8px}

/* Business cards */
.card{position:absolute;width:245px;height:139px;overflow:hidden}
.card-front{left:801px;top:506px;background:var(--paper)}
.card-front .dark{position:absolute;left:0;top:0;width:245px;height:109px;background:linear-gradient(180deg,#2b2b2e,#38383c)}
.card-front .brand-mark{left:95px;top:15px;width:51px;height:51px;border-color:#f2f2f2;border-width:1.6px}
.card-front .brand-name{left:0;width:245px;text-align:center;top:69px;font-size:17px;color:#f2f2f2}
.card-front .brand-tagline{left:0;width:245px;text-align:center;top:88px;font-size:6px;letter-spacing:.3em;color:#c9c9cc}
.card-front .regulatory{left:0;width:245px;text-align:center;top:117px;font-size:6.3px;line-height:8.6px;letter-spacing:.05em;color:var(--ink-soft)}

.card-back{left:801px;top:718px;background:var(--paper)}
.person{left:11px;top:12px;font-size:13px;font-weight:700;letter-spacing:.04em;color:#3a3d42}
.quals{left:11px;top:29px;font-size:8px;letter-spacing:.04em;color:#3a3d42}
.role{left:11px;top:59px;font-size:6.6px;line-height:9px;letter-spacing:.05em;color:var(--ink-soft)}
.card-back .brand-mark{left:169px;top:15px;width:62px;height:62px;border-width:1.8px}
.contact-bar{left:11px;top:98px;width:222px;height:9px;background:var(--slate);color:#fff;font-size:5.6px;line-height:9px;letter-spacing:.05em;padding-left:3px;white-space:nowrap}
.contact-bar b{font-weight:700}
.card-links{left:11px;top:112px;font-size:6.3px;line-height:9px;color:var(--ink);white-space:nowrap}
.card-links b{font-weight:700}
.card-motto{right:12px;top:112px;text-align:right;font-size:6.3px;line-height:9px;font-weight:700;color:var(--ink);white-space:nowrap}
</style>
</head>
<body>

<section class="letterhead">
  <div class="brand-mark lh-mark"></div>
  <div class="abs brand-name lh-name">CALDERSTONE WEALTH</div>
  <div class="abs brand-tagline lh-tagline">Strategic Financial Advice</div>

  <div class="abs motto">'Financial peace of mind'</div>
  <div class="abs entity trading">Kestrel Holdings Pty Ltd<br>ATF The Ashgrove Family<br>Trust T/AS Brightmere Financial</div>
  <div class="abs entity abn">ABN: 41 628 305 917</div>
  <div class="abs entity rep">Corporate Authorised<br>Representative of Meridian<br>Advisory Group Limited</div>

  <div class="abs letter-body">
    <p>Lorem ipsum dolor sit amet, consectetur adipiscing elit, sed do eiusmod tempor incididunt ut labore et dolore magna aliqua. In iaculis nunc sed augue lacus viverra vitae congue. Tempor orci eu lobortis elementum nibh tellus molestie. Nisl pretium fusce id velit ut. Platea dictumst vestibulum rhoncus est pellentesque elit ullamcorper. Laoreet id donec ultrices tincidunt arcu non. Turpis egestas maecenas pharetra convallis posuere morbi. Massa vitae tortor condimentum lacinia. Suspendisse interdum consectetur libero id. Proin fermentum leo vel orci porta non. Sed id semper risus in hendrerit gravida rutrum quisque non. Sagittis vitae et leo duis ut diam quam nulla. Amet justo donec enim diam vulputate ut. Diam donec adipiscing tristique risus nec feugiat in fermentum. Facilisis leo vel fringilla est. Tempor commodo ullamcorper a lacus vestibulum sed arcu non. Magna etiam tempor orci eu lobortis elementum nibh tellus.</p>
    <p>Massa sapien faucibus et molestie ac feugiat sed lectus vestibulum. Pellentesque adipiscing commodo elit at imperdiet dui accumsan sit. Bibendum neque egestas congue quisque egestas diam in arcu cursus. Nisi quis eleifend quam adipiscing vitae proin. Placerat vestibulum lectus mauris ultrices eros in cursus. Dolor sit amet consectetur adipiscing elit duis. Malesuada proin libero nunc consequat interdum varius sit amet mattis. Pretium vulputate sapien nec sagittis aliquam malesuada bibendum arcu. Morbi tristique senectus et netus et malesuada. Malesuada bibendum arcu vitae elementum curabitur vitae nunc. Amet volutpat consequat mauris nunc congue nisi vitae suscipit. Tincidunt ornare massa eget egestas purus viverra accumsan in. Risus in hendrerit gravida rutrum quisque non tellus orci. Fermentum leo vel orci porta.</p>
    <p>Sit amet facilisis magna etiam. Massa enim nec dui nunc mattis enim ut tellus. Ut placerat orci nulla pellentesque dignissim enim sit amet. Duis ut diam quam nulla porttitor massa. Ut porttitor leo a diam sollicitudin tempor. Felis eget velit aliquet sagittis. Fringilla phasellus faucibus scelerisque eleifend donec pretium vulputate sapien nec. Cursus metus aliquam eleifend mi in nulla. Euismod lacinia at quis risus sed vulputate odio ut. Tellus orci ac auctor augue mauris augue neque gravida. Consectetur adipiscing elit duis tristique sollicitudin nibh sit amet. Id donec ultrices tincidunt arcu. Vestibulum sed arcu non odio euismod lacinia. Pharetra et ultrices neque ornare aenean.</p>
  </div>

  <div class="abs signature" role="img" aria-label="Handwritten signature of the sender"></div>

  <svg class="abs footer-art" viewBox="0 0 525 127" aria-hidden="true">
    <defs>
      <linearGradient id="footerBand" x1="0" y1="0" x2="1" y2="0">
        <stop offset="0" stop-color="#4b5259"/>
        <stop offset="1" stop-color="#5d646b"/>
      </linearGradient>
    </defs>
    <path d="M0 0 H218 Q224 0 228 5 L246 24 H525 V32 H0 Z" fill="#333336"/>
    <rect x="0" y="32" width="525" height="95" fill="url(#footerBand)"/>
  </svg>

  <div class="abs footer-text web">www.brightmerefinancial.com.au<br>admin@brightmerefinancial.com.au</div>
  <div class="abs footer-text phones">P&nbsp; (07) 3555 0142<br>F&nbsp; (07) 3555 0187</div>
  <div class="abs footer-text address">Suite 4A, 18 Harlow St<br>Riverton QLD 4170<br>PO Box 3310<br>Riverton QLD 4170</div>
  <div class="abs footer-text licensee">Meridian Advisory Group Limited<br>ABN 52 118 407 633</div>
  <div class="abs footer-text licence">Australian Financial Services Licence<br>Licence Number 318 204<br>Principle Address: 210 Linden St<br>PO Box 1148 Melbourne VIC 3001</div>
</section>

<section class="card card-front">
  <div class="dark"></div>
  <div class="brand-mark"></div>
  <div class="abs brand-name">CALDERSTONE WEALTH</div>
  <div class="abs brand-tagline">Strategic Financial Advice</div>
  <div class="abs regulatory">Meridian Advisory Group Limited<br>Australian Financial Services Licensee License Number 318204</div>
</section>

<section class="card card-back">
  <div class="abs person">SAM TARRANT</div>
  <div class="abs quals">B.Ag.Ec. Dip F.P. CFP®</div>
  <div class="abs role">Managing Director<br>Authorised Representative</div>
  <div class="brand-mark"></div>
  <div class="abs contact-bar"><b>P:</b> (07) 3555 0142 &nbsp;|&nbsp; <b>M:</b> 0400 555 218 &nbsp;|&nbsp; <b>F:</b> (07) 3555 0187</div>
  <div class="abs card-links">sam@<b>brightmere</b>financial.com.au<br>www.<b>brightmere</b>financial.com.au</div>
  <div class="abs card-motto">Financial Peace Of Mind<br>A Referral Built Business</div>
</section>

</body>
</html>
```